AUDITING SERVICES FOR IMPORT/EXPORT/LOGISTICS

* PROCUREMENT OF PARTS / SERVICES
* BOAT POSITIONING

Industry/Entity Type

Auditing

Contact Information for Business Card

KTF CONSULTANTS
(WILLOW HARBOUR CRAFT PTY LTD) 17 THE ESPLANADE CORELLA SHORES
DAVID FENWICK 0418274603 LOUISE-JANE FENWICK 0418274681 (ON OPPOSITE SIDE)

```html
<!DOCTYPE html>
<html lang="en">
<head>
<meta charset="utf-8">
<title>KTF Consultants – Business Card</title>
<link rel="stylesheet" href="https://fonts.googleapis.com/css2?family=Exo+2:wght@400;500&display=swap">
<style>
  :root {
    --page-bg: #f4f4f4;
    --card-dark: #060709;
    --card-mid: #1b2029;
    --brand-blue-light: #4f6fe0;
    --silver: #d9dde3;
    --silver-dark: #7d838c;
    --text-white: #f2f3f5;
    --text-soft: #c9ccd2;
  }
  * { margin: 0; padding: 0; box-sizing: border-box; }
  html, body {
    width: 1200px;
    height: 900px;
    overflow: hidden;
    background: var(--page-bg);
  }
  .canvas {
    position: relative;
    width: 1200px;
    height: 900px;
  }
  .card {
    position: absolute;
    top: 291px;
    width: 520px;
    height: 318px;
    border-radius: 24px;
    overflow: hidden;
    background: radial-gradient(ellipse 70% 60% at 50% 40%, var(--card-mid) 0%, var(--card-dark) 75%);
    box-shadow: 0 10px 24px rgba(0,0,0,0.18);
  }
  .card--front { left: 50px; }
  .card--back { left: 630px; }

  .brand {
    position: absolute;
    left: 0; right: 0;
    text-align: center;
    font-family: "Exo 2", sans-serif;
  }
  .brand__name {
    color: var(--silver);
    font-weight: 500;
    letter-spacing: 1px;
    white-space: nowrap;
  }
  .brand__line {
    color: var(--text-soft);
    font-weight: 400;
    letter-spacing: 0.5px;
    white-space: nowrap;
  }

  .card--front .brand { top: 118px; }
  .card--front .brand__name { font-size: 34px; }
  .card--front .brand__line { font-size: 15px; margin-top: 10px; }

  .card--back .brand { top: 56px; }
  .card--back .brand__name { font-size: 28px; }
  .card--back .brand__line { font-size: 13px; margin-top: 8px; }

  .divider {
    position: absolute;
    left: 0; right: 0;
    top: 166px;
    height: 4px;
    background: linear-gradient(90deg, var(--silver-dark), var(--silver) 50%, var(--silver-dark));
  }

  .contacts {
    position: absolute;
    left: 26px; right: 26px;
    top: 186px;
    display: flex;
    justify-content: space-between;
    font-family: "Exo 2", sans-serif;
  }
  .contact { text-align: center; }
  .contact__name {
    color: var(--brand-blue-light);
    font-size: 15px;
    text-transform: uppercase;
    letter-spacing: 0.5px;
  }
  .contact__phone {
    color: var(--text-white);
    font-size: 20px;
    font-weight: 500;
    letter-spacing: 1.5px;
    margin-top: 2px;
  }
  .contact__email {
    color: var(--text-soft);
    font-size: 13px;
    margin-top: 2px;
  }
  .address {
    position: absolute;
    left: 0; right: 0;
    top: 274px;
    text-align: center;
    font-family: "Exo 2", sans-serif;
    font-size: 14px;
    color: var(--text-white);
    letter-spacing: 0.3px;
  }
</style>
</head>
<body>
<main class="canvas">

  <section class="card card--front" aria-label="Business card front">
    <div class="brand">
      <p class="brand__name">KTF Consultants</p>
      <p class="brand__line">Import · Export · Logistics Auditing</p>
    </div>
  </section>

  <section class="card card--back" aria-label="Business card back">
    <div class="brand">
      <p class="brand__name">KTF Consultants</p>
      <p class="brand__line">Import · Export · Logistics Auditing</p>
    </div>
    <div class="divider"></div>
    <div class="contacts">
      <div class="contact">
        <p class="contact__name">David Fenwick</p>
        <p class="contact__phone">(61) 418 274 603</p>
        <p class="contact__email">david@ktf.net.au</p>
      </div>
      <div class="contact">
        <p class="contact__name">Louise-Jane Fenwick</p>
        <p class="contact__phone">(61) 418 274 681</p>
        <p class="contact__email">louisejane@ktf.net.au</p>
      </div>
    </div>
    <p class="address">17 The Esplanade Corella Shores Qld 4519</p>
  </section>

</main>
</body>
</html>
```